NEW! Sports Supplement label
Vital Kinetic Laboratories
Project: NEW! Sports Supplement label
NEW! Sports Supplement label - Sports
Creative Brief
Looking for a new packaging design for a new line of products. This needs to be a clean label that delivers a scientific or medical feel in 3 colors with 4 lines for product descriptor sublines. <p><p> For Example: <p> • Muscle Recovery Acceleration <p> • Nitric Oxide Production <p> • Maximum Muscle Mass <p> • Improved Energy &amp; Focus <p><p> Use the following elements for presentation: <p><p> Name: VK260Q <p><p> 120 Capsules Dietary Supplement <p><p> The products are geared to Sports Supplements, Fat burners, preworkout supplements, sport drinks. <p><p> The fonts for the Product name and VKL logo must be destinctive elements and pop that adds value by providing consumers with instantly recognizable cues to help with the purchase decision making process. Preferrably reversed out white or black. <p> <p> Please see the following sites as example product labels for creative thought. They also provide actual full labels for your review: <p><p> http://www.plorvex.com/product/index.jsp?productId=48573920 http://www.plorvex.com/product/index.jsp?productId=48619375 http://www.plorvex.com/product/index.jsp?productId=48926054 <p><p> The label should be clean, in that it provides a clear, attractive space, with key information (4 line product descriptor mentioned above) on the front display panel necessary for a consumer to make a quick purchase decision. <p> The label should communicate a concise but informative message designed to make the consumer feel comfortable with the product by providing consumers with instantly recognizable cues (symbols of quality) to help with the purchase decision making process.
Sports
Sports nutrition products target a mass audience of consumers who have grown up knowing an active lifestyle has positive, long-term implications for health, fitness, weight management and longevity.
Please provide label design with color codes and in standard file formats with element layers. 2.75 x 7.00 4 x 9.375

```html
<!DOCTYPE html>
<html lang="en">
<head>
<meta charset="utf-8">
<title>VK260Q Dietary Supplement Label</title>
<link rel="stylesheet" href="https://fonts.googleapis.com/css2?family=Archivo+Black&family=Archivo+Narrow:wght@700&family=Ubuntu:wght@500;700&display=swap">
<style>
  :root {
    --blue-deep: #1b4f86;
    --blue-mid: #2f6fae;
    --blue-light: #5a97cf;
    --navy-text: #101a2c;
    --white: #ffffff;
    --red: #d3172c;
    --red-dark: #8e0c1a;
    --black: #050505;
    --chrome-hi: #ffffff;
    --chrome-mid: #bfc6cf;
    --chrome-low: #6d7682;
  }
  * { margin: 0; padding: 0; box-sizing: border-box; }
  html, body { width: 1200px; height: 929px; overflow: hidden; background: var(--white); }
  .label {
    position: relative;
    width: 1200px;
    height: 929px;
    overflow: hidden;
    background:
      repeating-linear-gradient(90deg, rgba(255,255,255,0.06) 0 3px, rgba(0,0,0,0.05) 3px 9px, rgba(255,255,255,0.03) 9px 22px, rgba(0,0,0,0.04) 22px 31px),
      linear-gradient(90deg, var(--blue-deep) 0%, var(--blue-mid) 20%, var(--blue-light) 45%, var(--blue-mid) 70%, var(--blue-deep) 100%);
  }
  .top-sheen {
    position: absolute; left: 0; top: 0; width: 1200px; height: 56px;
    background: linear-gradient(180deg, #f4f6f8 0%, #e3e8ee 40%, rgba(200,214,230,0.4) 75%, rgba(200,214,230,0) 100%);
  }
  .brand {
    position: absolute; left: 112px; top: 62px;
    font-family: "Archivo Black", sans-serif;
    color: var(--white);
    font-size: 96px; line-height: 96px;
    height: 96px;
    display: flex; align-items: center;
  }
  .brand-name {
    position: absolute; left: 116px; top: 162px;
    font-family: "Ubuntu", sans-serif; font-weight: 700;
    color: var(--white);
    font-size: 27px; line-height: 32px; letter-spacing: 0.3px;
  }
  .new-ribbon { position: absolute; left: 922px; top: 80px; width: 114px; height: 140px; }
  .product-name {
    position: absolute; left: 110px; top: 262px;
    font-family: "Archivo Black", sans-serif;
    font-size: 226px; line-height: 1; letter-spacing: -2px;
    transform: scaleX(0.89); transform-origin: left top;
    background: linear-gradient(180deg, var(--chrome-hi) 0%, var(--chrome-mid) 40%, var(--chrome-low) 52%, var(--chrome-mid) 70%, var(--chrome-hi) 100%);
    -webkit-background-clip: text; background-clip: text;
    color: transparent;
  }
  .descriptor {
    position: absolute; left: 380px; top: 462px;
    font-family: "Archivo Narrow", sans-serif; font-weight: 700;
    color: var(--navy-text);
    font-size: 60px; line-height: 1; letter-spacing: 1px;
  }
  .benefits {
    position: absolute; left: 118px; top: 604px;
    list-style: none;
    font-family: "Ubuntu", sans-serif; font-weight: 700;
    color: var(--white);
    font-size: 34px; line-height: 44px;
  }
  .benefits li::before { content: "\203A"; font-weight: 700; margin-right: 14px; }
  .count-badge {
    position: absolute; left: 930px; top: 758px; width: 170px; height: 160px;
    background: var(--black);
    border-radius: 22px;
    color: var(--white); text-align: center;
    font-family: "Ubuntu", sans-serif; font-weight: 700;
  }
  .count-number { display: block; font-size: 80px; line-height: 1; margin-top: 14px; }
  .count-unit { display: block; font-size: 23px; line-height: 1; margin-top: 6px; }
  .bottom-band { position: absolute; left: 0; bottom: 0; width: 1200px; height: 30px; background: var(--black); }
</style>
</head>
<body>
<div class="label">
  <div class="top-sheen"></div>
  <div class="brand">VKL</div>
  <div class="brand-name">VITAL KINETIC LABORATORIES</div>

  <svg class="new-ribbon" viewBox="0 0 114 140" aria-label="New">
    <polygon points="0,10 10,0 10,10" fill="var(--red-dark)"/>
    <polygon points="10,0 114,0 114,140 62,112 10,140" fill="var(--red)"/>
    <text x="62" y="74" text-anchor="middle" font-family="Ubuntu, sans-serif" font-weight="700" font-size="32" fill="#ffffff">NEW!</text>
  </svg>

  <div class="product-name">VK260Q</div>
  <div class="descriptor">DIETARY SUPPLEMENT</div>

  <ul class="benefits">
    <li>Muscle Recovery Acceleration</li>
    <li>NItric Oxide Production</li>
    <li>Maximum Musle Mass</li>
    <li>Improved Energy &amp; Focus</li>
  </ul>

  <div class="count-badge">
    <span class="count-number">30</span>
    <span class="count-unit">CAPSULES</span>
  </div>
  <div class="bottom-band"></div>
</div>
</body>
</html>
```